Car transport business

We need a new business card design. Attached is our old card sample. I would just like to adjust the logo colors (blue and red) to be brighter. I changed my name to the brighter red and the word dispatcher to a brighter blue as an example. But you can adjust those colors further. And then perhaps you can use the same colors for the card design but use your imagination.

As a suggestion so the card stands out I would like to add a clip art of car carrier truck. Attached are examples of that as well

```html
<!DOCTYPE html>
<html lang="en">
<head>
<meta charset="utf-8">
<title>Apex Haul – Business Card</title>
<link rel="stylesheet" href="https://fonts.googleapis.com/css2?family=Montserrat:wght@400;500;700&display=swap">
<style>
  :root {
    --page: #dddddd;
    --paper: #ffffff;
    --brand-blue: #175a87;
    --brand-blue-deep: #0f3f62;
    --brand-red: #c21d2b;
  }
  * { margin: 0; padding: 0; box-sizing: border-box; }
  html, body { width: 1200px; height: 1200px; overflow: hidden; }
  body {
    background: var(--page);
    font-family: "Montserrat", Arial, sans-serif;
    position: relative;
  }
  .card {
    position: absolute;
    left: 207px;
    width: 786px;
    height: 448px;
    overflow: hidden;
  }
  .card--front { top: 112px; background: var(--paper); }
  .card--back { top: 640px; background: var(--brand-blue); }

  .brand {
    position: absolute;
    display: flex;
    align-items: center;
    gap: 12px;
  }
  .brand__dot {
    width: 30px; height: 30px;
    border-radius: 50%;
    background: var(--brand-red);
  }
  .brand__name {
    font-weight: 700;
    letter-spacing: 1px;
    white-space: nowrap;
  }
  .card--front .brand { left: 52px; top: 66px; }
  .card--front .brand__name { font-size: 30px; color: var(--brand-blue); }

  .card--back .brand {
    left: 50%; top: 50%;
    transform: translate(-50%, -50%);
    gap: 20px;
  }
  .card--back .brand__dot { width: 60px; height: 60px; background: var(--brand-blue-deep); }
  .card--back .brand__name { font-size: 58px; color: var(--brand-blue-deep); letter-spacing: 2px; }

  .person {
    position: absolute;
    right: 52px;
    top: 208px;
    text-align: right;
  }
  .person__name {
    font-size: 39px;
    font-weight: 500;
    color: var(--brand-red);
    line-height: 1;
    letter-spacing: 0.5px;
  }
  .person__role {
    margin-top: 6px;
    font-size: 20px;
    color: var(--brand-blue);
    line-height: 1;
    letter-spacing: 0.5px;
  }
  .divider {
    position: absolute;
    left: 52px; top: 262px;
    width: 536px; height: 1.5px;
    background: var(--brand-red);
  }
  .side-tab {
    position: absolute;
    right: 0; top: 218px;
    width: 12px; height: 52px;
    background: var(--brand-blue);
  }

  .contact {
    position: absolute;
    left: 52px; top: 309px;
    list-style: none;
  }
  .contact li {
    display: flex;
    align-items: center;
    gap: 8px;
    height: 25px;
    font-size: 19px;
    color: var(--brand-blue);
  }
  .contact svg { width: 16px; height: 16px; flex: none; }

  .footer-bands {
    position: absolute;
    left: 0; bottom: 0;
    width: 786px; height: 48px;
  }
</style>
</head>
<body>

<section class="card card--front" aria-label="Card front">
  <div class="brand">
    <span class="brand__dot"></span>
    <span class="brand__name">APEX HAUL</span>
  </div>

  <div class="person">
    <p class="person__name">REMY CALDER</p>
    <p class="person__role">DISPATCHER</p>
  </div>
  <div class="divider"></div>
  <div class="side-tab"></div>

  <ul class="contact">
    <li>
      <svg viewBox="0 0 16 16" aria-hidden="true"><path d="M4 1.5l2.3 3.2-1.4 1.4c.8 1.9 2.2 3.4 4 4.3l1.4-1.4 3.2 2.3-1.3 2.6C7.3 13.5 2.5 8.7 1.5 3.2z" fill="none" stroke="#c21d2b" stroke-width="1.5" stroke-linejoin="round"/></svg>
      555-310-4827
    </li>
    <li>
      <svg viewBox="0 0 16 16" aria-hidden="true"><rect x="4" y="1.5" width="8" height="4" fill="#c21d2b"/><rect x="1" y="5.5" width="14" height="6" rx="1" fill="#c21d2b"/><rect x="4" y="9.5" width="8" height="5" fill="#fff" stroke="#c21d2b" stroke-width="1.2"/></svg>
      555-310-4890
    </li>
    <li>
      <svg viewBox="0 0 16 16" aria-hidden="true"><rect x="1.5" y="3.5" width="13" height="9" rx="1" fill="none" stroke="#c21d2b" stroke-width="1.5"/><path d="M2 4.5l6 4.5 6-4.5" fill="none" stroke="#c21d2b" stroke-width="1.5"/></svg>
      apexhaulco@mail.com
    </li>
  </ul>

  <svg class="footer-bands" viewBox="0 0 786 48" aria-hidden="true">
    <path d="M0 22 H455 L448 28 H0 Z" fill="var(--brand-red)"/>
    <path d="M0 36 H440 C460 36 470 30 490 20 C505 13 515 11 530 11 H786 V48 H0 Z" fill="var(--brand-blue)"/>
  </svg>
</section>

<section class="card card--back" aria-label="Card back">
  <div class="brand">
    <span class="brand__dot"></span>
    <span class="brand__name">APEX HAUL</span>
  </div>
</section>

</body>
</html>
```